Trash/recycling can & dumpster cleaning service

We power wash the inside and outside of trash/recycling cans & dumpsters. The water is collected and disposed of properly. We use environmentally safe products that leave your bins looking and smelling new.

Target Market(s)

Homeowners/renters, HOA's, Restaurant/Bars, Grocery stores, Hotel & Motels, Vacation homes, and neighborhoods with special rules to be allowed to live there.

Industry/Entity Type

Cleaning Service

Contact Information for Business Card

Bristle Bright Bins, Doug Pemberton-president-(608)555-0173, Marcus Telford-Vice President/treasurer-(608)555-0148, Lakemont, WI

Font styles to use
Serif

Requirements
Nice to have
• A picture of trash can (real or animated). The colors we would like to use is the same as the picture of Varo shoes in my images, sketches, or document section. Main color the aqua blue w/the bright fluorescent yellow and orange as accent colors.

```html
<!DOCTYPE html>
<html lang="en">
<head>
<meta charset="utf-8">
<title>Bristle Bright Bins – Business Card</title>
<link rel="stylesheet" href="https://fonts.googleapis.com/css2?family=Caladea:wght@400;700&display=swap">
<style>
  :root {
    --page: #ecebe6;
    --grass-light: #5fbf3a;
    --grass-mid: #3f9a26;
    --grass-dark: #2b7419;
    --aqua: #129b94;
    --aqua-light: #5cc8c6;
    --aqua-dark: #0d7f7a;
    --orange: #f59b12;
    --yellow: #f2ee2a;
    --can-green: #1f8a3c;
  }
  * { box-sizing: border-box; margin: 0; padding: 0; }
  html, body { width: 1200px; height: 1000px; overflow: hidden; }
  body {
    background: var(--page);
    font-family: "Caladea", Georgia, serif;
    position: relative;
  }
  .card {
    position: absolute;
    left: 280px;
    width: 640px;
    height: 372px;
    overflow: hidden;
    box-shadow: 0 6px 18px rgba(0,0,0,0.25);
  }
  .card--front { top: 90px; }
  .card--back { top: 530px; }

  .grass {
    position: absolute; inset: 0;
    background:
      radial-gradient(ellipse at 30% 30%, var(--grass-light), transparent 60%),
      radial-gradient(ellipse at 80% 70%, var(--grass-light), transparent 55%),
      linear-gradient(160deg, var(--grass-mid), var(--grass-dark));
  }
  .banner { position: absolute; display: block; }
  .card--front .banner { left: 34px; top: 88px; width: 572px; height: 84px; }
  .card--back .banner { left: 120px; top: 30px; width: 484px; height: 74px; }

  .brand-name {
    position: absolute;
    color: var(--orange);
    white-space: nowrap;
    text-align: center;
    text-shadow: 1px 1px 1px rgba(0,0,0,0.35);
  }
  .card--front .brand-name { left: 34px; width: 572px; top: 106px; font-size: 42px; line-height: 48px; }
  .card--back .brand-name { left: 120px; width: 484px; top: 46px; font-size: 36px; line-height: 42px; }

  .mascot {
    position: absolute;
    border-radius: 10px;
    background: radial-gradient(ellipse at 50% 45%, var(--can-green), #145f29 80%);
  }
  .card--front .mascot { left: 274px; top: 190px; width: 92px; height: 150px; }
  .card--back .mascot { left: 64px; top: 128px; width: 86px; height: 140px; z-index: 2; }

  .contact-band {
    position: absolute;
    left: 0; top: 158px; right: 20px; bottom: 0;
    background: var(--aqua);
    border-top: 5px solid var(--orange);
    border-right: 5px solid var(--orange);
  }
  .contact-list {
    position: absolute;
    left: 170px; top: 178px;
    list-style: none;
    color: var(--yellow);
    font-size: 21px;
    line-height: 23px;
    white-space: nowrap;
    z-index: 3;
  }
</style>
</head>
<body>

  <section class="card card--front" aria-label="Business card front">
    <div class="grass" role="img" aria-label="Sparkling green lawn background"></div>
    <svg class="banner" viewBox="0 0 572 84" aria-hidden="true">
      <defs>
        <linearGradient id="bannerFillFront" x1="0" y1="0" x2="0" y2="1">
          <stop offset="0" stop-color="#5cc8c6"/>
          <stop offset="0.5" stop-color="#129b94"/>
          <stop offset="1" stop-color="#0d7f7a"/>
        </linearGradient>
      </defs>
      <polygon points="0,42 34,4 538,4 572,42 538,80 34,80" fill="url(#bannerFillFront)"/>
    </svg>
    <p class="brand-name">Bristle Bright Bins</p>
    <div class="mascot" role="img" aria-label="Cartoon green wheeled trash can giving a thumbs up"></div>
  </section>

  <section class="card card--back" aria-label="Business card back">
    <div class="grass" role="img" aria-label="Sparkling green lawn background"></div>
    <svg class="banner" viewBox="0 0 484 74" aria-hidden="true">
      <defs>
        <linearGradient id="bannerFillBack" x1="0" y1="0" x2="0" y2="1">
          <stop offset="0" stop-color="#5cc8c6"/>
          <stop offset="0.5" stop-color="#129b94"/>
          <stop offset="1" stop-color="#0d7f7a"/>
        </linearGradient>
      </defs>
      <polygon points="0,37 30,4 454,4 484,37 454,70 30,70" fill="url(#bannerFillBack)"/>
    </svg>
    <p class="brand-name">Bristle Bright Bins</p>
    <div class="contact-band"></div>
    <div class="mascot" role="img" aria-label="Cartoon green wheeled trash can giving a thumbs up"></div>
    <ul class="contact-list">
      <li>President : Doug Pemberton</li>
      <li>Phone Number : (608)555-0173</li>
      <li>Vice President / Treasurer : Marcus Telford</li>
      <li>Phone Number : (608)555-0148</li>
      <li>Lakemont, WI</li>
    </ul>
  </section>

</body>
</html>
```